design cheese package for BRUVO

We want someone to give me some graphic designs for the cheese package. You shall not only design it on the basis of our product sizes, but also the design with my company Logo shall be novel and attactive. There are some pictures in the attachments: picture 1--3 for my product; picture 4 for my company Logo; picture 5--6 for your reference Thanks! please add the word BRUVO in the package design, thanks!

Industry/Entity Type

Product

```html
<!DOCTYPE html>
<html lang="en">
<head>
<meta charset="utf-8">
<title>BRUVO Sharp Cheddar Cheese Label</title>
<link rel="stylesheet" href="https://fonts.googleapis.com/css2?family=Alfa+Slab+One&display=swap">
<style>
  :root {
    --bg-center: #ffffff;
    --bg-edge: #e6e6e6;
    --band: #b97a30;
    --ink: #55290f;
    --ink-shadow: #e2b676;
    --band-text: #ffffff;
    --scene-sky: #bfe3f2;
    --scene-field: #8cbf4a;
  }
  html, body {
    margin: 0;
    padding: 0;
    width: 1200px;
    height: 857px;
    overflow: hidden;
  }
  .label {
    position: relative;
    width: 1200px;
    height: 857px;
    background: radial-gradient(ellipse at center, var(--bg-center) 40%, var(--bg-edge) 100%);
    font-family: "Alfa Slab One", Georgia, serif;
    color: var(--ink);
  }
  .band {
    position: absolute;
    left: 222px;
    width: 756px;
    background: var(--band);
  }
  .band--top { top: 51px; height: 138px; }
  .band--bottom {
    top: 729px;
    height: 78px;
    display: flex;
    align-items: center;
    justify-content: center;
  }
  .net-weight {
    margin: 0;
    color: var(--band-text);
    font-size: 25px;
    letter-spacing: 2px;
  }
  .farm-scene {
    position: absolute;
    top: 82px;
    left: 500px;
    width: 200px;
    height: 200px;
    background: linear-gradient(180deg, var(--scene-sky) 0%, var(--scene-sky) 45%, var(--scene-field) 100%);
  }
  .brand-name {
    position: absolute;
    top: 300px;
    left: 0;
    width: 100%;
    margin: 0;
    text-align: center;
    font-size: 74px;
    line-height: 1;
    letter-spacing: 28px;
    text-indent: 28px;
    color: var(--ink);
  }
  .product-title {
    margin: 0;
    font-weight: 400;
  }
  .product-title__line {
    position: absolute;
    left: 0;
    width: 100%;
    text-align: center;
    line-height: 1;
    text-shadow: 3px 3px 0 var(--ink-shadow);
  }
  .product-title__line--sharp { top: 494px; font-size: 92px; }
  .product-title__line--cheddar { top: 584px; font-size: 92px; }
  .product-title__line--cheese { top: 678px; font-size: 44px; letter-spacing: 2px; text-indent: 2px; }
</style>
</head>
<body>
  <main class="label">
    <div class="band band--top"></div>
    <div class="farm-scene" role="img" aria-label="Farm scene with a barn, rising sun and grazing cows"></div>
    <p class="brand-name">BRUVO</p>
    <h1 class="product-title">
      <span class="product-title__line product-title__line--sharp">SHARP</span>
      <span class="product-title__line product-title__line--cheddar">CHEDDAR</span>
      <span class="product-title__line product-title__line--cheese">CHEESE</span>
    </h1>
    <div class="band band--bottom">
      <p class="net-weight">Net WT 8OZ (226g)</p>
    </div>
  </main>
</body>
</html>
```